DovetailLeaf.com

Updated Website Structure for DovetailLea.com
1. Home Page

(Add social media links in footer or sidebar)
Suggested addition:

Stay Connected
Follow Dovetail Lea for daily encouragement, calming tools, and community stories.

[Facebook Icon] [Instagram Icon] [YouTube Icon]
@DovetailLeaOfficial

2. How It Works

(No major change — keep focused on process and trust building)

3. Ebook Store

(Add social links at the bottom of the page)

Want more free content?
Follow us on social media for sneak peeks, affirmations, and updates on new releases!

[Facebook] [Instagram] [YouTube]

4. Certification Page

(Optional social proof addition)

Connect with Certified Dovetail Leas
Join our online community and see real stories of growth and courage.

Follow us on social media to see how others are supporting each other:

5. Membership Tiers

(Keep page simple, but can include icons in footer)

6. About Me

Suggested addition:

Let’s Stay Connected
I love hearing from others walking this path.

Facebook: @DovetailLeaOfficial

Instagram: @DovetailLeaOfficial

YouTube: Dovetail Lea Channel

7. Disclosure Page

(Keep links in footer only for professional feel.)

8. Global Footer (Site-wide)

Every page should include a calming footer with:

Navigation links (Home | About Me | How It Works | Ebook Store | Certification | Membership | Disclosure)

Social media icons

Copyright info

Example footer text:

🌿 Walking with fear, choosing courage, calming the nervous system together.

© 2025 DovetailLea.com | All rights reserved

```html
<!DOCTYPE html>
<html lang="en">
<head>
<meta charset="utf-8">
<title>Dovetail Leas — Home</title>
<link href="https://fonts.googleapis.com/css2?family=Poppins:ital,wght@0,500;0,600;0,700;1,600&family=Lato:wght@400;700&family=Playfair+Display:ital@1&display=swap" rel="stylesheet">
<style>
  :root{
    --stage:#86749b;
    --ink:#2a0f2a;
    --mauve:#86749b;
    --nav-bg:#f6d2e2;
    --nav-edge:#f3bcd6;
    --ribbon:#bb9dc5;
    --hero-a:#f1b8d6;
    --hero-b:#ecc6dc;
    --section:#e8c6dc;
    --card:#f3d8e7;
    --footer-a:#eeb4d2;
    --footer-b:#ecc8dd;
    --soft:#f7e6ef;
  }
  *{box-sizing:border-box;margin:0;padding:0}
  html,body{width:1200px;height:1200px;overflow:hidden}
  body{background:var(--stage);font-family:'Lato',sans-serif;color:var(--ink);position:relative}
  .site{position:absolute;left:182px;top:27px;width:835px;height:1065px;overflow:hidden;background:var(--section)}
  .abs{position:absolute}

  .nav{left:0;top:0;width:835px;height:41px;background:var(--nav-bg);border-bottom:7px solid var(--nav-edge)}
  .nav-close{left:12px;top:9px;font-size:12px;font-weight:700}
  .nav-list{left:38px;top:10px;display:flex;gap:19px;font-size:10px;list-style:none}
  .nav-list li{display:flex;align-items:center;gap:5px}
  .nav-list svg{width:9px;height:9px;fill:var(--ink)}
  .theme-toggle{left:787px;top:12px;width:36px;height:18px;border-radius:9px;background:var(--soft)}
  .theme-toggle::before{content:"";position:absolute;left:3px;top:2px;width:14px;height:14px;border-radius:50%;background:var(--ink)}

  .ribbon{left:0;top:43px;width:835px;height:31px;background:linear-gradient(90deg,#c4a1c9,var(--ribbon));font-size:9.5px}
  .ribbon-text{top:10px}
  .pill{top:7px;height:20px;padding:0 10px;border-radius:10px;background:var(--ink);color:#fff;font-family:'Poppins',sans-serif;font-weight:600;font-size:8.5px;line-height:20px}
  .ribbon svg{top:10px;width:15px;height:11px;fill:var(--ink)}

  .hero{left:0;top:74px;width:835px;height:320px;background:linear-gradient(120deg,var(--hero-a),var(--hero-b))}
  .hero-art{left:47px;top:64px;width:308px;height:256px;border-radius:10px 10px 0 0;background:radial-gradient(circle at 50% 45%,#e9c4dc 0 28%,#b996b6 40%,var(--mauve) 62%)}
  .hero-title{left:380px;top:98px;font-family:'Poppins',sans-serif;font-weight:700;font-size:31px;line-height:48px;width:300px}
  .hero-copy{left:380px;top:209px;width:410px;font-size:11.5px;line-height:19px}
  .hero-btn{left:380px;top:265px;width:93px;height:33px;border-radius:17px;background:var(--mauve);color:#fff;font-family:'Poppins',sans-serif;font-weight:600;font-size:10px;text-align:center;line-height:33px}
  .dots{left:399px;top:304px;display:flex;gap:5px}
  .dots i{width:7px;height:7px;border-radius:50%;background:#f4dbe8}
  .dots i:first-child{width:9px;height:9px;margin-top:-1px;background:#fff}

  .how-title{left:0;top:429px;width:835px;text-align:center;font-family:'Poppins',sans-serif;font-weight:600;font-size:20.5px}
  .how-sub{left:0;top:470px;width:835px;text-align:center;font-size:11px}
  .card{top:532px;width:215px;height:199px;border-radius:12px;background:var(--card);text-align:center;box-shadow:0 0 14px rgba(200,150,190,.35)}
  .card svg{position:absolute;left:88px;top:28px;width:40px;height:32px;fill:var(--ink)}
  .card h3{position:absolute;left:0;top:84px;width:100%;font-family:'Poppins',sans-serif;font-weight:600;font-size:12px}
  .card p{position:absolute;left:14px;top:111px;width:187px;font-size:11px;line-height:17.5px}

  .footer{left:0;top:750px;width:835px;height:315px;background:linear-gradient(180deg,var(--footer-a),var(--footer-b));text-align:center}
  .brand{left:0;top:37px;width:835px;display:flex;justify-content:center;align-items:center;gap:9px;font-family:'Poppins',sans-serif;font-weight:600;font-size:18px;color:var(--mauve)}
  .brand i{width:16px;height:16px;border-radius:50%;background:var(--mauve)}
  .follow{left:0;top:81px;width:835px;font-family:'Playfair Display',serif;font-style:italic;font-size:10.5px}
  .socials{left:366px;top:116px;display:flex;gap:12px}
  .socials span{width:25px;height:25px;border-radius:50%;background:var(--mauve)}
  .mission-title{left:0;top:160px;width:835px;font-family:'Poppins',sans-serif;font-style:italic;font-weight:600;font-size:13px}
  .mission-quote{left:255px;top:192px;width:325px;font-family:'Playfair Display',serif;font-style:italic;font-size:11.5px;line-height:17.5px}
  .foot-links{left:0;top:246px;width:835px;display:flex;justify-content:center;gap:12.5px;font-size:10px;list-style:none}
  .copyright{left:0;top:284px;width:835px;font-size:8.5px}
</style>
</head>
<body>
<main class="site">
  <header class="nav abs">
    <span class="nav-close abs">✕</span>
    <ul class="nav-list abs">
      <li><svg viewBox="0 0 10 10"><path d="M5 0L0 5h1.5v5h2.5V7h2v3h2.5V5H10z"/></svg>Home</li>
      <li><svg viewBox="0 0 10 10"><circle cx="3.5" cy="5" r="3"/><circle cx="8" cy="3" r="2"/></svg>How It Works</li>
      <li><svg viewBox="0 0 10 10"><rect x="1.5" y="0" width="7" height="10" rx="1"/></svg>Ebooks</li>
      <li><svg viewBox="0 0 10 10"><circle cx="5" cy="3.5" r="3.2"/><path d="M3 6l-1 4 3-1.5L8 10 7 6z"/></svg>Certification</li>
      <li><svg viewBox="0 0 10 10"><circle cx="5" cy="3" r="2"/><circle cx="1.8" cy="3.8" r="1.4"/><circle cx="8.2" cy="3.8" r="1.4"/><path d="M1.5 10c0-3 7-3 7 0z"/></svg>Membership</li>
      <li><svg viewBox="0 0 10 10"><circle cx="5" cy="2.8" r="2.5"/><path d="M1 10c0-4.5 8-4.5 8 0z"/></svg>About</li>
      <li><svg viewBox="0 0 10 10"><path d="M1.5 0h4.5l2.5 2.5V10h-7z"/></svg>Disclosure</li>
      <li><svg viewBox="0 0 10 10"><rect x="0" y="1.5" width="10" height="7" rx="1"/></svg>Contact</li>
    </ul>
    <span class="theme-toggle abs" aria-label="Dark mode toggle"></span>
  </header>

  <div class="ribbon abs">
    <span class="ribbon-text abs" style="left:2px">Walking with fear. Choosing courage. Calming the nervous system together.</span>
    <span class="pill abs" style="left:331px">Learn more</span>
    <svg class="abs" style="left:442px" viewBox="0 0 15 11"><circle cx="7.5" cy="3" r="2.5"/><circle cx="2.5" cy="4" r="1.8"/><circle cx="12.5" cy="4" r="1.8"/><path d="M2 11c0-5 11-5 11 0z"/></svg>
    <span class="ribbon-text abs" style="left:469px">Join our supportive community of individuals on similar journeys</span>
    <span class="pill abs" style="left:752px">Join now</span>
  </div>

  <section class="hero abs">
    <div class="hero-art abs" role="img" aria-label="Heart emblem artwork with two women holding hands"></div>
    <h1 class="hero-title abs">Welcome to Dovetail Leas</h1>
    <p class="hero-copy abs">Walking with fear. Choosing courage. Your space for calm, community, and courage through anxiety.</p>
    <span class="hero-btn abs">Get Started</span>
    <div class="dots abs"><i></i><i></i><i></i></div>
  </section>

  <h2 class="how-title abs">How It Works</h2>
  <p class="how-sub abs">Discover the process of building trust and finding calm. Step-by-step guidance to help you on your journey.</p>

  <article class="card abs" style="left:194px">
    <svg viewBox="0 0 40 32"><circle cx="15" cy="8" r="7.5"/><path d="M2 31c0-12 26-12 26 0z"/><path d="M32 10h3v5h5v3h-5v5h-3v-5h-5v-3h5z"/></svg>
    <h3>Join Our Community</h3>
    <p>Sign up and become part of our supportive network of individuals on similar journeys.</p>
  </article>
  <article class="card abs" style="left:429px">
    <svg viewBox="0 0 40 32"><path d="M3 3c6-1 12 0 16 3v24c-4-2-10-3-16-2z"/><path d="M37 3c-6-1-12 0-16 3v24c4-2 10-3 16-2z"/></svg>
    <h3>Access Resources</h3>
    <p>Explore our library of ebooks, guides, and tools designed to help you manage anxiety.</p>
  </article>

  <footer class="footer abs">
    <div class="brand abs"><i></i>Dovetail Leas</div>
    <p class="follow abs">Follow us.</p>
    <div class="socials abs">
      <span aria-label="Social link one"></span><span aria-label="Social link two"></span><span aria-label="Social link three"></span>
    </div>
    <h4 class="mission-title abs">Mission Statement</h4>
    <p class="mission-quote abs">"Walking with fear. Choosing courage. Calming the nervous system together."</p>
    <ul class="foot-links abs">
      <li>Home</li><li>How It Works</li><li>Ebooks</li><li>Certification</li><li>Membership</li><li>About</li><li>Disclosure</li><li>Contact</li>
    </ul>
    <p class="copyright abs">© 2025 DovetailLeaf.com. All rights reserved.</p>
  </footer>
</main>
</body>
</html>
```